Packing for Disinfectant wipes

Design the Packinging for new Disinfectant wipes. Wipes are for cleaning and disinfectanting hard surfaces and equipment. There are 100 wipes to the packet (size 230mm x 300mm). The company is called Norbeck Supplies and is supplier of consumable products to healthcare companies. Wipes are not for use on humans/baby. Packaging size as per attachment.
Industry/Entity Type
Healthcare
Requirements
Nice to have
- Packaging need ingredients list and directions for use

```html
<!DOCTYPE html>
<html lang="en">
<head>
<meta charset="utf-8">
<title>Norbeck Supplies – Disinfectant Wipes Pack</title>
<link href="https://fonts.googleapis.com/css2?family=Open+Sans:ital,wght@0,600;0,700;1,600;1,700&family=Noto+Sans:wght@700&display=swap" rel="stylesheet">
<style>
  :root{
    --navy:#0b6db3;
    --deep:#0a72b8;
    --mid:#1e8bca;
    --sky:#24aee0;
    --cyan:#2cb0e2;
    --pale:#a3cfe8;
    --label:#22aee0;
    --white:#ffffff;
    --contact-light:#27a8df;
  }
  html,body{margin:0;padding:0;overflow:hidden;background:#fff;}
  .pack{
    position:relative;width:1024px;height:1200px;overflow:hidden;
    font-family:"Open Sans",sans-serif;
  }
  .pack-art{position:absolute;inset:0;}
  .flip{position:absolute;left:0;width:1024px;transform:rotate(180deg);text-align:center;}
  .supplier{
    top:36px;font-family:"Noto Sans",sans-serif;font-weight:700;color:var(--navy);
    font-size:14px;line-height:23.5px;
  }
  .supplier .small{font-size:12.5px;color:var(--contact-light);line-height:18px;font-weight:700;}
  .title-flipped{
    top:268px;font-size:72px;font-weight:700;font-style:italic;color:var(--navy);line-height:90px;
  }
  .claim{
    position:absolute;top:455px;left:0;width:1024px;text-align:center;
    font-size:26px;font-weight:700;font-style:italic;color:var(--navy);
  }
  .brand-label{
    position:absolute;left:380px;top:560px;width:266px;text-align:center;
    color:var(--white);font-weight:600;font-size:31px;line-height:36px;
  }
  .open-tab{position:absolute;left:482px;top:660px;width:60px;text-align:center;color:var(--white);font-size:8px;font-weight:700;}
  .count{
    position:absolute;left:740px;top:682px;width:100px;text-align:center;color:var(--white);
    font-weight:700;
  }
  .count .num{font-size:32px;line-height:36px;display:block;}
  .count .unit{font-size:13px;font-style:italic;line-height:16px;display:block;}
  .title-main{
    position:absolute;top:835px;left:0;width:1024px;text-align:center;
    font-size:73px;font-weight:700;font-style:italic;color:var(--white);line-height:100px;
  }
  .ingredients{
    position:absolute;left:171px;top:1006px;width:683px;height:157px;box-sizing:border-box;
    border:2.5px dashed var(--white);text-align:center;color:var(--white);
  }
  .ingredients h2{margin:22px 0 10px;font-size:20px;font-weight:700;}
  .ingredients p{margin:0;font-size:16.5px;font-style:italic;font-weight:600;line-height:24px;}
  .corner-brand{
    position:absolute;left:876px;top:1096px;width:90px;text-align:center;color:var(--white);
    font-size:15px;font-weight:600;line-height:17px;
  }
</style>
</head>
<body>
<div class="pack">
  <svg class="pack-art" width="1024" height="1200" viewBox="0 0 1024 1200" aria-hidden="true">
    <defs>
      <linearGradient id="base" x1="0" y1="0" x2="0" y2="1">
        <stop offset="0.35" stop-color="#0a72b8"/>
        <stop offset="0.62" stop-color="#0c74ba"/>
        <stop offset="1" stop-color="#24aee0"/>
      </linearGradient>
      <linearGradient id="top" x1="0" y1="0" x2="0" y2="1">
        <stop offset="0.7" stop-color="#ffffff"/>
        <stop offset="1" stop-color="#dcebf6"/>
      </linearGradient>
    </defs>
    <rect class="base-fill" width="1024" height="1200" fill="url(#base)"/>
    <path class="top-panel" d="M0,0 H1024 V290 Q834,520 646,590 L380,590 Q190,520 0,290 Z" fill="url(#top)"/>
    <g class="bands-left">
      <path d="M0,290 Q190,520 380,590 Q190,545 0,375 Z" fill="var(--pale)"/>
      <path d="M0,375 Q190,545 380,592 Q190,565 0,465 Z" fill="var(--cyan)"/>
      <path d="M0,730 Q150,650 380,604 Q150,680 0,822 Z" fill="var(--cyan)"/>
      <path d="M0,822 Q150,680 380,606 Q140,725 0,903 Z" fill="var(--pale)"/>
    </g>
    <g class="bands-right" transform="translate(1024,0) scale(-1,1)">
      <path d="M0,290 Q190,520 378,590 Q190,545 0,375 Z" fill="var(--pale)"/>
      <path d="M0,375 Q190,545 378,592 Q190,565 0,465 Z" fill="var(--cyan)"/>
      <path d="M0,730 Q150,650 378,604 Q150,680 0,822 Z" fill="var(--cyan)"/>
      <path d="M0,822 Q150,680 378,606 Q140,725 0,903 Z" fill="var(--pale)"/>
    </g>
    <path class="label-dashes" d="M384,514 H640 Q655,514 655,530 V670 Q655,685 640,685 H580 Q565,685 555,693 Q512,720 470,693 Q460,685 445,685 H384 Q370,685 370,670 V530 Q370,514 384,514 Z"
      fill="none" stroke="#a3cfe8" stroke-width="2.5" stroke-dasharray="12 7"/>
    <path class="label-tab" d="M392,522 H633 Q645,522 645,534 V664 Q645,676 633,676 H575 Q562,676 552,684 Q512,708 472,684 Q462,676 449,676 H392 Q380,676 380,664 V534 Q380,522 392,522 Z"
      fill="var(--label)" stroke="#6cc8ec" stroke-width="1.5"/>
    <path class="open-arrow" d="M512,664 L522,682 H502 Z" fill="#fff"/>
  </svg>

  <div class="flip supplier">
    <div>Supplier:</div>
    <div>Brightwell Hygiene Technology Co.,Ltd</div>
    <div>Maple Park industry zone, Eastfield, Westbrook City, Harbor Province, Examplia</div>
    <div>Telephone:&nbsp; (00) 0100-5550111</div>
    <div>Fax:&nbsp; (00) 100 5550333</div>
    <div class="small">e-mail address of person responsible for this SDS: info@brightwellcare.example</div>
    <div class="small">Emergency telephone number(with hours of operation): 00-100-5550222</div>
  </div>

  <div class="flip title-flipped">Disinfectant wipes</div>

  <div class="claim">Kill 99 % of Viruses &amp; Bacteria</div>

  <div class="brand-label">Norbeck<br>Supplies</div>
  <div class="open-tab">OPEN</div>

  <div class="count"><span class="num">100</span><span class="unit">WET WIPES</span></div>

  <div class="title-main">Disinfectant wipes</div>

  <section class="ingredients">
    <h2>INGREDIENTS :</h2>
    <p>AQUA, Didecyldimethylammonium chloride,Benzalkonium Chloride,<br>
    Phenoxyethanol, PEG40 Hydrogenated Casor Oil, Ethylhexylglycerin,<br>
    Disodium EDTA, Perfume</p>
  </section>

  <div class="corner-brand">Norbeck<br>Supplies</div>
</div>
</body>
</html>
```